E-Book-Design für Ejakulationstraining
Zielgruppe
Für ein E-Book im Bereich Ejakulationstraining benötigen wir ein Cover.
Aufgabenstellung
Titel: Handbuch
10 Tipps zum länger durchhalten
Es sollte in diese Richtung gehen: https://www.buchwarenlager.de/STAHL-TEMPO-Performance-Liebeskraft-Liebesleben/dp/K42X19QMTZ/ref=sr_1_1?__mk_de_DE=%C3%85M%C3%85%C5%BD%C3%95%C3%91&keywords=Stahl+Duo&qid=1566887931&s=gateway&sr=8-1

```html
<!DOCTYPE html>
<html lang="de">
<head>
<meta charset="utf-8">
<title>Handbuch – 10 Tipps zum länger durchhalten</title>
<link href="https://fonts.googleapis.com/css2?family=Fira+Sans+Condensed:wght@300;700&family=Montserrat:wght@300;800&display=swap" rel="stylesheet">
<style>
  :root {
    --page: #ffffff;
    --band: #1a1a1a;
    --ink-light: #ffffff;
    --photo-top: #4a4752;
    --photo-mid: #6b6470;
    --photo-low: #2c2c36;
    --green-deep: #0b6b33;
    --green-lime: #93c41f;
  }
  * { margin: 0; padding: 0; box-sizing: border-box; }
  html, body {
    width: 838px; height: 1200px; overflow: hidden;
    background: var(--page);
  }
  .cover {
    position: absolute; left: 99px; top: 99px;
    width: 641px; height: 1004px;
    overflow: hidden;
    background: var(--photo-low);
  }
  .series-band {
    position: absolute; left: 0; top: 0; width: 100%; height: 50px;
    background: var(--band);
    display: flex; align-items: center; justify-content: center;
    font-family: "Montserrat", sans-serif;
    font-size: 21px; letter-spacing: 0.5px;
    color: var(--ink-light);
  }
  .series-band strong, .publisher strong { font-weight: 800; }
  .series-band span, .publisher span { font-weight: 300; }
  .cover-photo {
    position: absolute; left: 0; top: 50px; width: 100%; height: 954px;
    background:
      radial-gradient(ellipse at 65% 40%, #9a8e95 0%, rgba(154,142,149,0) 45%),
      linear-gradient(180deg, var(--photo-top) 0%, var(--photo-mid) 45%, var(--photo-low) 100%);
  }
  .title-badge {
    position: absolute; left: 82px; top: 449px;
    width: 476px; height: 476px; border-radius: 50%;
    background: linear-gradient(135deg, var(--green-deep) 15%, var(--green-lime) 50%, var(--green-deep) 85%);
    text-align: center;
    font-family: "Fira Sans Condensed", sans-serif;
    color: var(--ink-light);
  }
  .title-main {
    position: absolute; left: 0; right: 0; top: 106px;
    font-weight: 700; font-size: 112px; line-height: 1; letter-spacing: -1px;
  }
  .title-sub {
    position: absolute; left: 0; right: 0; top: 228px;
    font-weight: 300; font-size: 64px; line-height: 68px;
  }
  .publisher {
    position: absolute; left: 0; right: 0; top: 958px;
    text-align: center;
    font-family: "Montserrat", sans-serif;
    font-size: 21px; letter-spacing: 0.5px;
    color: var(--ink-light);
  }
</style>
</head>
<body>
  <div class="cover">
    <div class="cover-photo" role="img" aria-label="Foto eines leidenschaftlich umarmenden Paares vor grauem Hintergrund"></div>
    <header class="series-band"><strong>HAND</strong><span>BUCH</span></header>
    <div class="title-badge">
      <h1 class="title-main">10 TIPPS</h1>
      <p class="title-sub">ZUM LÄNGER<br>DURCHHALTEN</p>
    </div>
    <footer class="publisher"><strong>MUSTER</strong><span>VERLAG</span></footer>
  </div>
</body>
</html>
```